Velmira website

A clean uncluttered design that shows at glance that we are in the Media and design and publishing business.

We would like to see designs that use colours that show warmth and quality.

The website should show:
- products
- projects

These should be displaxed in spaces that we can add or interchanges with new products or projects.

Target Market(s)

Business and project managers and buyers and authors.

Industry/Entity Type

Business

Requirements
Must have
• Good colours. Not too strong, not weak, but reflecting quality.

```html
<!DOCTYPE html>
<html lang="en">
<head>
<meta charset="utf-8">
<title>Velmira Book Publishes</title>
<link href="https://fonts.googleapis.com/css2?family=Open+Sans+Condensed:ital,wght@0,700;1,300&family=Open+Sans:ital,wght@0,400;0,600;0,700;0,800;1,400;1,600;1,700;1,800&display=swap" rel="stylesheet">
<style>
:root{
  --blue:#0d57b0;
  --blue-dark:#083f86;
  --blue-text:#1a5fb4;
  --page:#efefef;
  --panel:#ffffff;
  --line:#d7d7d7;
  --text:#3b3b3b;
  --red:#d9262b;
  --wood:#dcb37b;
  --wood-dark:#b3834b;
  --grass:#5aa52a;
}
*{box-sizing:border-box;margin:0;padding:0}
html,body{width:709px;height:1200px;overflow:hidden}
body{background:linear-gradient(#e9e9e9,#f3f3f3 100px,#efefef);font-family:"Open Sans",sans-serif;color:var(--text);position:relative}
.abs{position:absolute}

/* header */
.brand{left:68px;top:10px;display:flex;align-items:center;gap:8px}
.brand-name{font-weight:800;font-size:25px;color:var(--blue-dark);line-height:1}
.brand-sub{font-size:10px;font-weight:700;color:#222;letter-spacing:.5px}
.brand-mark{width:30px;height:30px;border:2px solid var(--blue);border-radius:3px}
.header-books{left:272px;top:20px;width:208px;height:47px;border-radius:2px 2px 0 0;
  background:
   linear-gradient(rgba(255,255,255,.25),rgba(255,255,255,0) 40%,rgba(0,0,0,.18)),
   linear-gradient(90deg,rgba(239,239,239,1) 0,rgba(239,239,239,0) 12%,rgba(239,239,239,0) 88%,rgba(239,239,239,1)),
   linear-gradient(90deg,#6e6e6e,#8c7a6a 20%,#a8453a 35%,#7c6a5a 45%,#c85aa8 55%,#6c8aa0 65%,#8a8a8a 80%,#b9b9b9)}
.account{right:61px;top:11px;display:flex;gap:14px}
.account a{font-size:10px;font-weight:600;color:#222;text-decoration:none;border:1px solid #aaa;border-radius:9px;padding:1px 8px 1px 18px;background:#fff;position:relative}
.account a::before{content:"";position:absolute;left:5px;top:3px;width:9px;height:9px;border-radius:50% 50% 2px 2px;background:#333}
.account a.signin{color:var(--blue)}
.account a.signin::before{background:var(--blue)}
.socials{right:60px;top:38px;display:flex;gap:5px}
.socials span{width:15px;height:15px;border-radius:50%;background:#8a8f96}
.socials span:first-child{background:var(--blue)}

/* nav */
.nav{left:60px;top:67px;width:590px;height:64px;box-shadow:0 4px 8px rgba(0,0,0,.22)}
.nav-top{height:32px;background:linear-gradient(#1667c4,var(--blue));display:flex;padding-left:30px}
.nav-top a{color:#fff;font-size:11.5px;font-weight:600;text-decoration:none;padding:8px 14px;border-right:1px solid rgba(255,255,255,.25)}
.nav-home{position:absolute;left:0;top:0;width:30px;height:64px;background:var(--blue-dark);display:flex;align-items:center;justify-content:center;z-index:1}
.nav-bottom{height:32px;background:linear-gradient(#4a4a4a,#2a2a2a);display:flex;align-items:center;padding-left:42px;gap:10px}
.pill{height:18px;border-radius:9px;font-size:7.5px;font-style:italic;color:#fff;display:flex;align-items:center;padding:0 9px;white-space:nowrap}
.pill.dark{background:#111;border:1px solid #666}
.pill.blue{background:var(--blue);border:1px solid #5a8fd6}
.search{width:168px;height:18px;border-radius:9px;background:#222;border:1px solid #666;display:flex;align-items:center;font-size:7px;color:#888;font-style:italic;padding-left:8px;position:relative}
.search .cat{position:absolute;right:26px;color:#ccc}
.search .go{position:absolute;right:-1px;top:-1px;width:20px;height:18px;border-radius:9px;background:var(--blue);display:flex;align-items:center;justify-content:center}
.cart{color:#fff;font-size:9px;font-weight:600;margin-left:8px;display:flex;align-items:center;gap:3px}
.basket{right:-6px;top:14px;width:44px;height:44px;background:linear-gradient(#f8de5a,#e0a414);clip-path:polygon(8% 22%,100% 10%,86% 100%,20% 100%);z-index:2}

/* banner */
.banner{left:60px;top:150px;width:588px;height:248px;filter:drop-shadow(0 2px 3px rgba(0,0,0,.3))}
.banner-frame{position:absolute;inset:0;background:#fff;clip-path:path("M0 4 Q147 -4 294 12 Q441 -4 588 4 L588 242 Q441 252 294 236 Q147 252 0 242 Z")}
.banner-art{position:absolute;left:4px;top:4px;width:580px;height:240px;clip-path:path("M0 4 Q145 -4 290 12 Q435 -4 580 4 L580 232 Q435 242 290 226 Q145 242 0 232 Z");
  background:
   radial-gradient(ellipse 70px 90px at 60px 150px,rgba(236,150,60,.85),rgba(200,60,50,.5) 60%,rgba(0,0,0,0)),
   radial-gradient(ellipse 80px 120px at 545px 120px,rgba(80,120,210,.8),rgba(220,70,120,.45) 55%,rgba(0,0,0,0)),
   radial-gradient(ellipse 90px 120px at 190px 140px,rgba(40,90,40,.55),rgba(0,0,0,0) 70%),
   radial-gradient(ellipse at 55% 40%,#9bd656,#5aa52a 55%,#2f7a18)}
.banner-title{position:absolute;left:252px;top:26px;font-family:"Open Sans Condensed",sans-serif;font-size:40px;font-weight:700;color:#3f8a1c;text-shadow:0 1px 0 #d9f2b4,0 2px 3px rgba(0,0,0,.35)}
.banner-author{position:absolute;left:298px;top:92px;font-size:14px;font-style:italic;font-weight:600;color:#111}
.banner-price{position:absolute;left:292px;top:110px;font-size:29px;font-style:italic;font-weight:800;color:#111;letter-spacing:-.5px}
.buy{position:absolute;left:324px;top:160px;width:112px;height:34px;background:linear-gradient(#1a6ccc,var(--blue-dark));border:2px solid #fff;box-shadow:0 2px 4px rgba(0,0,0,.35);color:#fff;font-size:14px;font-weight:800;font-style:italic;display:flex;align-items:center;padding-left:9px}
.dots{position:absolute;right:0;top:104px;width:14px;height:56px;background:var(--blue);border-radius:7px 0 0 7px;display:flex;flex-direction:column;justify-content:space-around;align-items:center;padding:5px 0}
.dots i{width:5px;height:5px;border-radius:50%;background:#fff}

/* panels */
.panel{background:var(--panel);border:1px solid var(--line);box-shadow:0 1px 4px rgba(0,0,0,.15)}
.panel-head{background:linear-gradient(#1466c2,var(--blue));color:#fff;font-weight:700;font-size:11px;padding:6px 9px}
.products{left:62px;top:422px;width:408px;height:602px;background:radial-gradient(ellipse at 50% 45%,#fff 60%,#ececec)}
.products .panel-head{font-size:13px;height:26px;padding:3px 9px}
.shelf{position:absolute;left:14px;width:382px}
.shelf-books{display:flex;gap:18px;padding-left:18px;position:relative;z-index:1}
.cover{width:74px;height:93px;border:2px solid #fff;box-shadow:0 1px 4px rgba(0,0,0,.45),2px 0 0 #e4e4e4;
  background:
   linear-gradient(90deg,rgba(0,0,0,.3),rgba(0,0,0,0) 9%,rgba(255,255,255,.08) 50%,rgba(0,0,0,.15)),
   linear-gradient(160deg,var(--c1),var(--c2))}
.board{height:22px;margin-top:-3px;background:linear-gradient(#efd2a4,var(--wood) 35%,var(--wood-dark));clip-path:polygon(2% 0,98% 0,100% 100%,0 100%);box-shadow:0 3px 4px rgba(0,0,0,.25)}
.pegs{position:relative;height:10px}
.pegs i{position:absolute;top:0;width:4px;height:9px;background:linear-gradient(#cfcfcf,#9a9a9a);border-radius:1px}
.view-all{position:absolute;right:0;bottom:0;background:var(--blue);color:#fff;font-size:8px;font-weight:600;padding:5px 8px}

.login{left:489px;top:422px;width:157px;height:142px}
.field{margin:6px 12px 0;height:18px;border:1px solid var(--line);font-size:7px;font-style:italic;color:#888;padding:4px 6px}
.btn{display:inline-block;background:var(--blue);color:#fff;font-size:9px;font-weight:700;font-style:italic;padding:3px 9px;border:1px solid #fff;outline:1px solid var(--blue)}
.small{font-size:7.5px;color:#555;line-height:11px}
.small em{color:var(--red);font-style:normal}

.review{left:489px;top:582px;width:157px;height:202px}
.rev-item{display:flex;gap:8px;padding:7px 6px;border-bottom:1px solid #e6e6e6}
.thumb{width:36px;height:44px;border:2px solid #fff;box-shadow:0 0 2px rgba(0,0,0,.45);flex:none;background:linear-gradient(160deg,var(--c1),var(--c2))}
.rev-title{font-size:9px;color:var(--blue-text);font-weight:600}
.rev-price{font-size:7px;color:#333}
.stars{font-size:12px;color:var(--blue);letter-spacing:-1px;line-height:14px}
.stars b{color:#777;font-weight:400}

.best{left:489px;top:802px;width:157px;height:222px}
.select{margin:8px 7px 0;height:18px;border:1px solid var(--line);font-size:7px;font-style:italic;color:#666;padding:4px 6px;position:relative}
.select::after{content:"▾";position:absolute;right:0;top:0;width:16px;height:16px;background:var(--blue);color:#fff;font-size:8px;text-align:center;line-height:16px;font-style:normal}
.best-main{display:flex;gap:7px;padding:9px 6px}
.best-cover{width:64px;height:80px;background:linear-gradient(90deg,rgba(0,0,0,.2),rgba(0,0,0,0) 10%),linear-gradient(160deg,#f3e3b8,#e0b25a 55%,#8aa0b0);border:2px solid #fff;box-shadow:0 0 3px rgba(0,0,0,.45)}
.rank{font-size:16px;font-weight:800;color:var(--blue)}
.best-title{font-size:9px;color:var(--blue-text);font-weight:600}
.carousel{display:flex;align-items:center;gap:6px;padding:4px 3px;border-top:1px solid #e6e6e6}
.mini{width:36px;height:42px;border:2px solid #fff;box-shadow:0 0 2px rgba(0,0,0,.4);background:linear-gradient(160deg,var(--c1),var(--c2))}
.arrow{font-size:11px;color:#333}

/* footer */
.footer{left:0;top:1044px;width:709px;height:132px;background:#e6e6e6;border-top:1px solid #dcdcdc}
.f-col{position:absolute;top:15px}
.f-divider{position:absolute;top:10px;width:1px;height:104px;background:#f6f6f6;box-shadow:-1px 0 0 #d6d6d6}
.f-head{font-size:10px;font-weight:600;color:var(--blue-text);margin-bottom:3px}
.f-col ul{list-style:none}
.f-col li{font-size:7.5px;line-height:16px;color:#555}
.f-col li::before{content:"▪ ";color:#999}
.f-col.first li:first-child{color:var(--blue-text)}
.f-socials{display:flex;gap:5px;margin:6px 0 8px 4px}
.f-socials span{width:15px;height:15px;border-radius:50%;background:#8a8f96}
.share{display:flex;gap:10px}
.share span{font-size:7.5px;font-weight:600;border:1px solid #bbb;background:#fff;padding:1px 5px;color:var(--blue)}
.share span.r{color:var(--red)}
.share i{font-style:normal;color:#666;font-weight:400;margin-left:6px}
.input{width:172px;height:19px;border:1px solid #ccc;background:#f2f2f2;font-size:7px;font-style:italic;color:#888;padding:4px 6px;margin-top:6px}
.sub{margin:6px 0 0 96px;background:var(--blue);color:#fff;font-size:8px;font-weight:700;padding:4px 9px;display:inline-block;outline:1px solid var(--blue);border:1px solid #fff}
.f-logo{left:268px;top:1136px;width:170px;height:42px;background:var(--page);clip-path:polygon(12% 0,88% 0,100% 100%,0 100%);display:flex;align-items:center;justify-content:center;gap:5px}
.f-logo b{font-size:16px;font-weight:800;color:var(--blue-dark)}
.f-logo span{width:16px;height:16px;border:2px solid var(--blue);border-radius:2px}
.copy{left:0;top:1182px;width:709px;text-align:center;font-size:7.5px;color:#444}
.copy a{color:var(--blue-text);text-decoration:none}
</style>
</head>
<body>

<header>
  <div class="abs brand">
    <div><div class="brand-name">Velmira</div><div class="brand-sub">Book Publishes</div></div>
    <span class="brand-mark"></span>
  </div>
  <div class="abs header-books" role="img" aria-label="Row of book spines standing on a shelf"></div>
  <div class="abs account"><a href="#">Login</a><a href="#" class="signin">Sign In</a></div>
  <div class="abs socials"><span></span><span></span><span></span><span></span><span></span><span></span></div>
</header>

<nav class="abs nav">
  <div class="nav-home">
    <svg width="18" height="18" viewBox="0 0 18 18"><path d="M2 9 9 2l7 7M4 8v8h4v-5h2v5h4V8" fill="none" stroke="#000" stroke-width="2"/></svg>
  </div>
  <div class="nav-top">
    <a href="#">About Us</a><a href="#">Books</a><a href="#">Products</a><a href="#">Projects</a><a href="#">Author Registration</a><a href="#" style="border:0">Contact Us</a>
  </div>
  <div class="nav-bottom">
    <span class="pill dark">All Categories ▾</span>
    <div class="search">Search...<span class="cat">All Categories ▾</span>
      <span class="go"><svg width="9" height="9" viewBox="0 0 9 9"><circle cx="5" cy="4" r="2.6" fill="none" stroke="#fff" stroke-width="1.2"/><path d="M3 6 1 8" stroke="#fff" stroke-width="1.2"/></svg></span>
    </div>
    <span class="pill blue">Advance Saerch</span>
    <span class="pill blue" style="margin-left:18px">Cart Item 0</span>
    <span class="cart">
      <svg width="18" height="14" viewBox="0 0 18 14"><path d="M0 1h3l2 8h10l2-6H5" fill="none" stroke="#fff" stroke-width="1.4"/><circle cx="7" cy="12" r="1.2" fill="#fff"/><circle cx="14" cy="12" r="1.2" fill="#fff"/></svg>Cart ▾
    </span>
  </div>
  <div class="abs basket" role="img" aria-label="Shopping basket"></div>
</nav>

<section class="abs banner">
  <div class="banner-frame"></div>
  <div class="banner-art" role="img" aria-label="Girl reading a book on a grass field between stacks of colourful books">
    <div class="banner-title">Selling eBooks</div>
    <div class="banner-author">Author: Marlow, Peter,</div>
    <div class="banner-price">Price: £ 0.00</div>
    <div class="buy">Buy Now
      <svg width="28" height="18" viewBox="0 0 28 18" style="margin-left:8px"><path d="M1 2h4l3 10h13l3-8H7" fill="none" stroke="#fff" stroke-width="2"/><circle cx="10" cy="16" r="1.5" fill="#fff"/><circle cx="19" cy="16" r="1.5" fill="#fff"/></svg>
    </div>
    <div class="dots"><i></i><i></i><i></i><i></i></div>
  </div>
</section>

<section class="abs panel products">
  <div class="panel-head">Our Product</div>
  <div class="shelf" style="top:38px">
    <div class="shelf-books">
      <div class="cover" role="img" aria-label="Book cover" style="--c1:#6f8f4a;--c2:#2c3d2a"></div>
      <div class="cover" role="img" aria-label="Book cover" style="--c1:#e33a3f;--c2:#b81a22"></div>
      <div class="cover" role="img" aria-label="Book cover" style="--c1:#f4efe6;--c2:#c9b09a"></div>
      <div class="cover" role="img" aria-label="Book cover" style="--c1:#e3c07a;--c2:#7a6a48"></div>
    </div>
    <div class="board"></div>
    <div class="pegs"><i style="left:42px"></i><i style="left:336px"></i></div>
  </div>
  <div class="shelf" style="top:174px">
    <div class="shelf-books">
      <div class="cover" role="img" aria-label="Book cover" style="--c1:#f6d24a;--c2:#e7a923"></div>
      <div class="cover" role="img" aria-label="Book cover" style="--c1:#c9c0ad;--c2:#7c6e5e"></div>
      <div class="cover" role="img" aria-label="Book cover" style="--c1:#a9c6a8;--c2:#4e7a62"></div>
      <div class="cover" role="img" aria-label="Book cover" style="--c1:#6f8ea0;--c2:#2e3e4a"></div>
    </div>
    <div class="board"></div>
    <div class="pegs"><i style="left:42px"></i><i style="left:336px"></i></div>
  </div>
  <div class="shelf" style="top:310px">
    <div class="shelf-books">
      <div class="cover" role="img" aria-label="Book cover" style="--c1:#8aa6c2;--c2:#1e4f86"></div>
      <div class="cover" role="img" aria-label="Book cover" style="--c1:#f19a3a;--c2:#1a6aa8"></div>
      <div class="cover" role="img" aria-label="Book cover" style="--c1:#d23a3a;--c2:#6e1a1e"></div>
      <div class="cover" role="img" aria-label="Book cover" style="--c1:#c9d6e0;--c2:#3a5470"></div>
    </div>
    <div class="board"></div>
    <div class="pegs"><i style="left:42px"></i><i style="left:336px"></i></div>
  </div>
  <div class="shelf" style="top:446px">
    <div class="shelf-books">
      <div class="cover" role="img" aria-label="Book cover" style="--c1:#f1dcc0;--c2:#b98a55"></div>
      <div class="cover" role="img" aria-label="Book cover" style="--c1:#e6edf2;--c2:#7aa0bc"></div>
      <div class="cover" role="img" aria-label="Book cover" style="--c1:#6a4030;--c2:#1e1410"></div>
      <div class="cover" role="img" aria-label="Book cover" style="--c1:#e23a3a;--c2:#a8151c"></div>
    </div>
    <div class="board"></div>
    <div class="pegs"><i style="left:42px"></i><i style="left:336px"></i></div>
  </div>
  <div class="view-all">View All books</div>
</section>

<aside>
  <section class="abs panel login">
    <div class="panel-head">Login</div>
    <div class="field">User name:</div>
    <div class="field">Password:</div>
    <div style="margin:10px 12px 4px"><span class="btn">Login</span></div>
    <div class="small" style="padding-left:12px">Not a registered author?<br>Register now &nbsp;/&nbsp; <em>Forgot password</em></div>
  </section>

  <section class="abs panel review">
    <div class="panel-head">Review</div>
    <div class="rev-item"><div class="thumb" role="img" aria-label="Book cover" style="--c1:#f4f6f8;--c2:#8fb0d0"></div><div><div class="rev-title">Lorem ipsum dolor sit</div><div class="rev-price">Price: $ 0.00</div><div class="stars">★★★★★</div></div></div>
    <div class="rev-item"><div class="thumb" role="img" aria-label="Book cover" style="--c1:#e8c79a;--c2:#9a6a42"></div><div><div class="rev-title">Lorem ipsum dolor sit</div><div class="rev-price">Price: $ 0.00</div><div class="stars">★★★<b>★★</b></div></div></div>
    <div class="rev-item" style="border:0"><div class="thumb" role="img" aria-label="Book cover" style="--c1:#a7b98e;--c2:#3a5236"></div><div><div class="rev-title">Lorem ipsum dolor sit</div><div class="rev-price">Price: $ 0.00</div><div class="stars">★★★<b>★★</b></div></div></div>
  </section>

  <section class="abs panel best">
    <div class="panel-head">Bestsellers</div>
    <div class="select">Books</div>
    <div class="best-main">
      <div class="best-cover" role="img" aria-label="Featured book cover"></div>
      <div>
        <div class="rank">#1</div>
        <div class="best-title">Lorem ipsum</div>
        <div class="rev-price" style="margin-top:3px">By: ipsum dolor</div>
        <div class="rev-price">Price: $ 0.00</div>
        <div class="stars">★★★★★</div>
      </div>
    </div>
    <div class="carousel">
      <span class="arrow">‹</span>
      <div class="mini" role="img" aria-label="Book cover" style="--c1:#f0d8a8;--c2:#b98a4a"></div>
      <div class="mini" role="img" aria-label="Book cover" style="--c1:#f4c4a8;--c2:#c4704a"></div>
      <div class="mini" role="img" aria-label="Book cover" style="--c1:#dfe4c0;--c2:#8a9a5a"></div>
      <span class="arrow">›</span>
    </div>
  </section>
</aside>

<footer>
  <div class="abs footer">
    <div class="f-col first" style="left:62px">
      <div class="f-head">eBook</div>
      <ul><li>Home</li><li>About Us</li><li>eBooks</li><li>Free Books</li><li>Printed Books</li></ul>
    </div>
    <div class="f-divider" style="left:148px"></div>
    <div class="f-col" style="left:163px;top:30px">
      <ul><li>New Authors</li><li>Author Registration</li><li>Terms of Use</li><li>Privacy</li><li>Contact Us</li></ul>
    </div>
    <div class="f-divider" style="left:256px"></div>
    <div class="f-col" style="left:290px">
      <div class="f-head">Keep Up with the latest</div>
      <div class="f-socials"><span></span><span></span><span></span><span></span><span></span><span></span></div>
      <div class="share"><span>Chirper<i>33</i></span><span class="r">Circlet<i>33</i></span></div>
    </div>
    <div class="f-col" style="left:470px">
      <div class="f-head">Connect To News Letter</div>
      <div class="input">Name</div>
      <div class="input">Email</div>
      <div class="sub">Subcribe Now</div>
    </div>
  </div>
  <div class="abs f-logo"><b>Velmira</b><span></span></div>
  <div class="abs copy">© 2013 <a href="#">Velmira Book</a> - All Right Recevied</div>
</footer>

</body>
</html>
```